The Gemstone Craft Studio Sales Business Card

The goal of this project is to create a interactive & effective business card design for SALES purposes with the intention to get customer on to our website and make a purchase or contact us about a product or service.
Website: WWW.FENWORKSHOP.COM
LocalListPro: https://g.page/FenWORKSHOP?gm
Pagebook & Snapgrid: @THEBRIMORECRAFTSTUDIO
Phone # & Text Message & Chatwire Message: +1(555) 418-2963
Email: HELLO@FENWORKSHOP.COM
Location: 2871 Marbury Lane Suite 412 Brookhaven, OR
(It would be necessary to have the appropriate ticker/icon for each social media platform as well as the location ticker and phone / messaging icons instead of spelling the words out.)
It is important to have the company logo and details but with an emphasis toward website. Feel free to also completely make one design your way and completely custom as you feel best.
The Gemstone Craft Studio is a Provider of Luxury Goods & Services such as: Custom Jewelry Design, Jewelry Repairs & Cleaning, Designer Jewelry, Luxury Gifts, 24 Karat Gold, 22 Karat Gold Jewelry, Diamond Jewelry, Insured Jewelry Appraisals, Loose Gemstones & Diamonds, Supporting Sustainability
Target Market(s)
People looking to invest in precious metals and gemstones as well as people looking to find a gift for a loved one for a special occasion. Customers looking to Custom Design Jewelry.
Contact Information for Business Card
Font styles to use
Other font styles liked:
- w.e you want
Colors
Designer to choose colors to be used in the design.
Requirements
Must have
- Website: WWW.FENWORKSHOP.COM
- LocalListPro: https://g.page/FenWORKSHOP?gm
- Pagebook & Snapgrid: @THEBRIMORECRAFTSTUDIO
- Phone # & Text Message & Chatwire Message: +1(555) 418-2963
- Email: HELLO@FENWORKSHOP.COM
- Location: 2871 Marbury Lane Suite 412 Brookhaven, OR
- (It would be necessary to have the appropriate ticker/icon for each social media platform as well as the location ticker and phone / messaging icons instead of spelling the words out.)
- It is important to have the company logo and details but with an emphasis toward website. Feel free to also completely make one design your way and completely custom as you feel best.
Nice to have
- The Gemstone Craft Studio is a Provider of Luxury Goods & Services such as: Custom Jewelry Design, Jewelry Repairs & Cleaning, Designer Jewelry, Luxury Gifts, 24 Karat Gold, 22 Karat Gold Jewelry, Diamond Jewelry, Insured Jewelry Appraisals, Loose Gemstones & Diamonds, Supporting Sustainability

```html
<!DOCTYPE html>
<html lang="en">
<head>
<meta charset="utf-8">
<title>The Gemstone Craft Studio – Business Card</title>
<link rel="stylesheet" href="https://fonts.googleapis.com/css2?family=Open+Sans:wght@400;600&family=Libre+Baskerville:wght@700&display=swap">
<style>
  :root {
    --brand-red: #ea202d;
    --brand-red-light: #f22a3a;
    --brand-gold: #f9d54f;
    --card-white: #ffffff;
    --ink: #2b2b2b;
    --rule: #8a8a8a;
    --backdrop: #d6d6d6;
  }
  * { margin: 0; padding: 0; box-sizing: border-box; }
  html, body { width: 1200px; height: 800px; overflow: hidden; }
  body {
    background: var(--backdrop);
    font-family: "Open Sans", Arial, sans-serif;
    position: relative;
  }
  .card {
    position: absolute;
    top: 284px;
    width: 430px;
    height: 238px;
    overflow: hidden;
  }

  /* Front */
  .card-front {
    left: 110px;
    background: radial-gradient(circle at 30% 45%, var(--brand-red-light), var(--brand-red) 60%);
  }
  .front-mark {
    position: absolute;
    left: 0; right: 0;
    top: 48px;
    display: flex;
    flex-direction: column;
    align-items: center;
    gap: 16px;
  }
  .front-mark .mark-dot {
    width: 58px; height: 58px;
    border-radius: 50%;
    background: var(--brand-gold);
  }
  .front-mark .brand-name {
    color: var(--card-white);
    font-family: "Libre Baskerville", Georgia, serif;
    font-weight: 700;
    font-size: 19px;
    text-align: center;
    line-height: 1.3;
  }
  .front-url {
    position: absolute;
    left: 0; right: 0;
    top: 202px;
    text-align: center;
    color: var(--card-white);
    font-size: 10px;
    letter-spacing: 2.2px;
  }

  /* Back */
  .card-back {
    left: 638px;
    background: var(--card-white);
  }
  .back-brand {
    position: absolute;
    left: 62px;
    top: 118px;
    width: 130px;
    color: var(--brand-red);
    font-family: "Libre Baskerville", Georgia, serif;
    font-weight: 700;
    font-size: 12.5px;
    line-height: 1.3;
    text-align: center;
  }
  .back-divider {
    position: absolute;
    left: 196px;
    top: 68px;
    width: 1px;
    height: 102px;
    background: var(--rule);
  }
  .contact-list {
    position: absolute;
    left: 216px;
    top: 78px;
    list-style: none;
  }
  .contact-item {
    display: flex;
    align-items: center;
    height: 21px;
    color: var(--ink);
    font-size: 11px;
  }
  .contact-item.handle { font-size: 8.5px; }
  .contact-item svg {
    width: 13px; height: 13px;
    margin-right: 9px;
    flex: none;
  }
  .gold-rule {
    position: absolute;
    left: 0; right: 0;
    top: 209px;
    height: 2px;
    background: var(--brand-gold);
  }
  .address-band {
    position: absolute;
    left: 0; right: 0;
    top: 212px;
    height: 26px;
    background: var(--brand-red);
    color: var(--card-white);
    font-size: 11px;
    display: flex;
    align-items: center;
    justify-content: center;
    gap: 7px;
  }
  .address-band svg { width: 11px; height: 13px; }
</style>
</head>
<body>

<section class="card card-front">
  <div class="front-mark">
    <span class="mark-dot"></span>
    <p class="brand-name">The Gemstone<br>Craft Studio</p>
  </div>
  <p class="front-url">www.fenworkshop.com</p>
</section>

<section class="card card-back">
  <p class="back-brand">The Gemstone Craft Studio</p>
  <span class="back-divider"></span>

  <ul class="contact-list">
    <li class="contact-item">
      <svg viewBox="0 0 24 24" fill="none" stroke="#ea202d" stroke-width="1.6" stroke-linejoin="round"><path d="M5 3h4l2 5-2.5 1.5a11 11 0 0 0 6 6L16 13l5 2v4a2 2 0 0 1-2 2A16 16 0 0 1 3 5a2 2 0 0 1 2-2z"/></svg>
      <span>+1(555) 418-2963</span>
    </li>
    <li class="contact-item">
      <svg viewBox="0 0 24 24" fill="none" stroke="#ea202d" stroke-width="1.6"><rect x="2" y="5" width="20" height="14"/><path d="M2 5l10 8 10-8M2 19l7-7M22 19l-7-7"/></svg>
      <span>hello@fenworkshop.com</span>
    </li>
    <li class="contact-item">
      <svg viewBox="0 0 24 24" fill="none" stroke="#ea202d" stroke-width="1.5"><circle cx="12" cy="12" r="9"/><ellipse cx="12" cy="12" rx="4" ry="9"/><path d="M3 12h18M4.5 7.5h15M4.5 16.5h15"/></svg>
      <span>www.fenworkshop.com</span>
    </li>
    <li class="contact-item handle">
      <svg viewBox="0 0 24 24" fill="none" stroke="#ea202d" stroke-width="1.8"><rect x="3" y="3" width="18" height="18" rx="4"/></svg>
      <span>@THEBRIMORECRAFTSTUDIO</span>
    </li>
  </ul>

  <span class="gold-rule"></span>
  <p class="address-band">
    <svg viewBox="0 0 20 24" fill="none" stroke="#ffffff" stroke-width="1.8"><path d="M10 23s8-8 8-14a8 8 0 0 0-16 0c0 6 8 14 8 14z"/><circle cx="10" cy="9" r="3"/></svg>
    <span>2871 Marbury Lane Suite 412 Brookhaven, OR</span>
  </p>
</section>

</body>
</html>
```